Verlune Magician

I want the business card for my business to give to people who watch that later I will be employed to show magic here is my website http://www.verlunemagicien-exemple.fr/I want the interesting design , i am very opened for formal and informal, I watch a lot of design so don't stick to the common shape and form but i hope it can also be produced the thing to write on will be the same as in picture that i will upload , i also will upload the logo for you that so can be easy to useDenis CostilleMagicianMAGICIAN VERLUNE 17 rue des Tilleuls - 25000 BESANÇON contact@verlunemagicien-exemple.fr tel. 0381 476 093 tel. 0664 219 570

```html
<!DOCTYPE html>
<html lang="fr">
<head>
<meta charset="utf-8">
<title>Verlune Magicien – Carte de visite</title>
<link rel="stylesheet" href="https://fonts.googleapis.com/css2?family=Roboto:wght@300;400;700&display=swap">
<style>
  :root {
    --board: #a97c54;
    --paper: #ffffff;
    --ink: #050505;
    --accent: #e0262b;
    --art-dark: #111111;
    --art-light: #3a3a3a;
  }
  * { margin: 0; padding: 0; box-sizing: border-box; }
  html, body { width: 1200px; height: 1200px; overflow: hidden; }
  body { background: var(--board); font-family: "Roboto", Arial, sans-serif; color: var(--ink); position: relative; }

  .card { position: absolute; left: 190px; width: 780px; height: 460px; background: var(--paper); overflow: hidden; }
  .card--front { top: 85px; }
  .card--back { top: 600px; }

  .identity { position: absolute; left: 42px; top: 50px; }
  .identity__name { font-size: 36px; font-weight: 700; letter-spacing: -0.3px; line-height: 1; }
  .identity__role { font-size: 22px; font-weight: 400; line-height: 1.05; margin-top: 3px; }

  .contact { position: absolute; left: 42px; list-style: none; }
  .contact--phones { top: 160px; }
  .contact--online { top: 260px; }
  .contact li { display: flex; align-items: center; font-size: 22px; line-height: 25px; height: 25px; margin-bottom: 1px; }
  .contact--online li:last-child { margin-top: 3px; }
  .contact svg { width: 15px; height: 15px; margin-right: 9px; flex: none; }

  .portrait { position: absolute; border-radius: 46% 46% 18% 18%; background: linear-gradient(180deg, var(--art-light) 0%, var(--art-dark) 55%); }
  .card--front .portrait { left: 515px; top: 45px; width: 170px; height: 210px; }
  .card--back .portrait { left: 308px; top: 82px; width: 180px; height: 230px; }

  .brand { position: absolute; font-weight: 300; letter-spacing: 1px; line-height: 1; text-align: center; }
  .card--front .brand { left: 500px; width: 200px; top: 265px; font-size: 35px; }
  .card--back .brand { left: 298px; width: 200px; top: 316px; font-size: 37px; }

  .sweep { position: absolute; left: 0; top: 0; width: 780px; height: 460px; }

  .tagline { position: absolute; left: 0; top: 414px; width: 780px; height: 30px; background: var(--ink); color: var(--paper); }
  .tagline span { position: absolute; top: 0; line-height: 30px; font-size: 19px; letter-spacing: 13px; }
</style>
</head>
<body>

  <section class="card card--front" aria-label="Recto de la carte">
    <div class="identity">
      <h1 class="identity__name">LUCIEN MARBEC</h1>
      <p class="identity__role">MAGICIAN</p>
    </div>

    <ul class="contact contact--phones">
      <li>
        <svg viewBox="0 0 16 16" aria-hidden="true"><rect x="0.5" y="0.5" width="15" height="15" fill="none" stroke="var(--accent)" stroke-width="0.6"/><path d="M4 2.5l2 2.3-1 1.3c.7 1.7 2 3 3.7 3.7l1.3-1 2.3 2-1 2c-4.6-.4-8.4-4.2-8.8-8.8z" fill="var(--ink)"/></svg>
        0381 476 093
      </li>
      <li>
        <svg viewBox="0 0 16 16" aria-hidden="true"><rect x="0.5" y="0.5" width="15" height="15" fill="none" stroke="var(--accent)" stroke-width="0.6"/><path d="M3 4h10v2H3z M3.5 7h9l1 6h-11z" fill="var(--ink)"/><circle cx="8" cy="10" r="1.6" fill="var(--paper)"/></svg>
        0664 219 570
      </li>
    </ul>

    <ul class="contact contact--online">
      <li>
        <svg viewBox="0 0 16 16" aria-hidden="true"><rect x="0.5" y="0.5" width="15" height="15" fill="none" stroke="var(--accent)" stroke-width="0.6"/><rect x="3" y="4.5" width="10" height="7" fill="var(--ink)"/><path d="M3 4.5l5 4 5-4" fill="none" stroke="var(--paper)" stroke-width="0.8"/></svg>
        verlunemagicien@exemple.fr
      </li>
      <li>
        <svg viewBox="0 0 16 16" aria-hidden="true"><circle cx="8" cy="8" r="5.5" fill="none" stroke="var(--ink)" stroke-width="1.4"/><ellipse cx="8" cy="8" rx="2.3" ry="5.5" fill="none" stroke="var(--ink)" stroke-width="1.1"/><path d="M2.5 8h11" stroke="var(--ink)" stroke-width="1.1"/></svg>
        www.verlunemagicien-exemple.fr
      </li>
      <li>
        <svg viewBox="0 0 16 16" aria-hidden="true"><rect x="0.5" y="0.5" width="15" height="15" fill="none" stroke="var(--accent)" stroke-width="0.6"/><path d="M8 2.5l6 5.5h-2v5.5H9.5V10h-3v3.5H4V8H2z" fill="var(--ink)"/></svg>
        17 rue des Tilleuls - 25000 BESANÇON
      </li>
    </ul>

    <div class="portrait" role="img" aria-label="Illustration en noir et blanc du magicien en veste tenant une carte à jouer"></div>
    <p class="brand">VERLUNE</p>

    <svg class="sweep" viewBox="0 0 780 460" aria-hidden="true">
      <polygon points="0,424 780,350 780,359 0,434" fill="var(--ink)"/>
      <polygon points="0,439 780,365 780,460 0,460" fill="var(--ink)"/>
    </svg>
  </section>

  <section class="card card--back" aria-label="Verso de la carte">
    <div class="portrait" role="img" aria-label="Illustration en noir et blanc du magicien en veste tenant une carte à jouer"></div>
    <p class="brand">VERLUNE</p>
    <div class="tagline">
      <span style="left:48px">MAKING</span>
      <span style="left:240px">EVENTS</span>
      <span style="left:426px">UNFORGETTABLE</span>
    </div>
  </section>

</body>
</html>
```